Veltrano - Mechanic/Collision Center Business Card

We're looking for a business card design for our mechanic/ collision repair shop.

Can be with colours or monochromatic.

See the attached files.

Many thanks

```html
<!DOCTYPE html>
<html lang="pt">
<head>
<meta charset="utf-8">
<title>Veltrano – Business Card</title>
<link rel="stylesheet" href="https://fonts.googleapis.com/css2?family=Arimo:wght@400;700&family=Montserrat:wght@400;700&display=swap">
<style>
  :root{
    --page:#e4e5e7;
    --card:#f6f6f5;
    --ink:#16191e;
    --text:#3a3d42;
    --brand-blue:#1b6a9c;
    --accent-blue:#1e8fd0;
    --band:#151a20;
    --back:#1a1f25;
    --back-text:#c9ccd0;
    --back-rule:#6b7078;
  }
  *{margin:0;padding:0;box-sizing:border-box}
  html,body{width:1200px;height:900px;overflow:hidden}
  body{background:var(--page);font-family:"Arimo",sans-serif;position:relative}

  .card{
    position:absolute;left:230px;width:740px;height:422px;
    overflow:hidden;box-shadow:0 2px 6px rgba(0,0,0,.14);
  }

  /* back side */
  .card--back{top:20px;background:var(--back);font-family:"Montserrat",sans-serif;
    display:flex;flex-direction:column;align-items:center;justify-content:center}
  .back-mark{display:flex;align-items:center;gap:12px}
  .back-mark__dot{width:34px;height:34px;border-radius:50%;background:var(--accent-blue)}
  .back-mark__name{font-size:46px;font-weight:700;color:#f2f3f4;letter-spacing:1px;line-height:1}
  .person-name{margin-top:46px;font-size:26px;font-weight:700;color:var(--accent-blue);letter-spacing:1.5px}
  .person-rule{margin-top:12px;width:50px;height:2px;background:var(--back-rule)}
  .person-phone{margin-top:14px;font-size:15px;color:var(--back-text);letter-spacing:.5px}

  /* front side */
  .card--front{top:458px;background:var(--card)}
  .brand-mark{position:absolute;left:36px;top:98px;display:flex;align-items:center;gap:11px}
  .brand-mark__dot{width:32px;height:32px;border-radius:50%;background:var(--accent-blue)}
  .brand-mark__name{font-size:45px;font-weight:700;color:var(--ink);letter-spacing:1px;line-height:1}
  .company-name{position:absolute;left:35px;top:229px;font-size:26px;font-weight:700;
    color:var(--brand-blue);letter-spacing:1px}
  .company-rule{position:absolute;left:35px;top:267px;width:13px;height:2px;background:var(--accent-blue)}
  .contact-list{position:absolute;left:35px;top:278px;list-style:none}
  .contact-list li{display:flex;align-items:center;height:25px;font-size:15.5px;color:var(--text)}
  .contact-list svg{width:13px;height:13px;margin-right:9px;flex:none}
  .contact-list small{font-size:12.6px;margin-left:4px}
  .address{position:absolute;right:21px;top:293px;text-align:right;font-size:15.5px;color:var(--text)}
  .address p{height:31px;display:flex;align-items:center;justify-content:flex-end}
  .address__label{color:var(--accent-blue);margin-right:4px}
  .address svg{width:13px;height:16px;margin-left:11px}
  .wave{position:absolute;left:0;bottom:0;width:740px;height:66px}
</style>
</head>
<body>
  <section class="card card--back">
    <div class="back-mark">
      <span class="back-mark__dot"></span>
      <span class="back-mark__name">VELTRANO</span>
    </div>
    <h2 class="person-name">Rui Matos</h2>
    <span class="person-rule"></span>
    <p class="person-phone">+351 912407356 (or just 912407356)</p>
  </section>

  <main class="card card--front">
    <div class="brand-mark">
      <span class="brand-mark__dot"></span>
      <span class="brand-mark__name">VELTRANO</span>
    </div>

    <h1 class="company-name">Veltrano, LDA</h1>
    <span class="company-rule"></span>

    <ul class="contact-list">
      <li>
        <svg viewBox="0 0 24 24" aria-hidden="true"><path fill="#16191e" d="M6.6 2.5l3 3.2-1.8 2.6c1.2 2.6 3.3 4.7 5.9 5.9l2.6-1.8 3.2 3-2 3.1C10.6 18.2 5.8 13.4 3.5 6.6z"/><path fill="none" stroke="#16191e" stroke-width="1.6" d="M14 3.5a6.5 6.5 0 0 1 6.5 6.5M14 7a3 3 0 0 1 3 3"/></svg>
        +351 214550182 <small>(or just 214550182)</small>
      </li>
      <li>
        <svg viewBox="0 0 24 24" aria-hidden="true"><rect x="2" y="5" width="20" height="14" fill="#16191e"/><path d="M4.5 8l7.5 5.5L19.5 8" fill="none" stroke="#f6f6f5" stroke-width="2"/></svg>
        veltrano.oficina@correio.pt
      </li>
      <li>
        <svg viewBox="0 0 24 24" aria-hidden="true"><circle cx="12" cy="12" r="10" fill="#16191e"/></svg>
        www.veltrano-auto.pt
      </li>
    </ul>

    <div class="address">
      <p><span class="address__label">Postal code:</span> 1900-118 Lisboa</p>
      <p>Rua das Oficinas, 42
        <svg viewBox="0 0 18 24" aria-hidden="true"><path fill="#16191e" d="M9 1a7.5 7.5 0 0 0-7.5 7.5C1.5 14 9 23 9 23s7.5-9 7.5-14.5A7.5 7.5 0 0 0 9 1zm0 10.5a3 3 0 1 1 0-6 3 3 0 0 1 0 6z"/></svg>
      </p>
    </div>

    <svg class="wave" viewBox="0 0 1060 95" preserveAspectRatio="none" aria-hidden="true">
      <path fill="var(--accent-blue)" d="M0 6 C200 50 420 48 640 20 C820 -2 960 -4 1060 18 L1060 32 C960 12 820 14 640 34 C420 60 200 62 0 22 Z"/>
      <path fill="var(--band)" d="M0 36 C200 74 420 72 640 44 C820 24 960 20 1060 40 L1060 95 L0 95 Z"/>
    </svg>
  </main>
</body>
</html>
```